Consulting and Personal Growth company needs instagram design

Design of Instagram feed.
Please see attached:
1. Design brief with all details and mood board
2. Posts texts
3. Brand logo and colors

Objective:
Design Instagram feed for The Lumen Compass so that the posts flow visually while each post looks beautiful by itself. The posts have the following order:

THEME: 1 PURPOSE - 3 posts
HEALTH - 3 posts
MIND - 3 posts
VISION - 3 posts
Every post will be posted independently (not in groups of 3)
Use @thelumencompass in all posts. (See post texts in attachment)

Target Market(s)

Business owners and executives, men and women who want to maximize their potential and impact.

Industry/Entity Type

Consulting

Font styles to use
Other font styles liked:
• Avenir

Requirements
Must have
• Clean, professional design
• Beautiful flow of posts in feed
• Eye-catching independent posts
• Feed is not disrupted when adding a new post
• Use @thelumencompass in all posts.
Nice to have
• Logo "star" can be used in posts if it helps build branding but not mandatory.
Should not have
• Each post independent with no flow/beautiful design of feed.

```html
<!DOCTYPE html>
<html lang="en">
<head>
<meta charset="utf-8">
<title>The Lumen Compass – Purpose Posts</title>
<link href="https://fonts.googleapis.com/css2?family=Amatic+SC:wght@400;700&family=Questrial&family=Shadows+Into+Light&display=swap" rel="stylesheet">
<style>
  :root {
    --page: #ffffff;
    --ink: #3a3a3a;
    --band-light: #5bb8e0;
    --band: #43a3cc;
    --paper-light: #efefed;
    --paper-blush: #e6d6cf;
    --paper-mid: #bdbdbd;
    --paper-dark: #8e8e8e;
  }
  * { margin: 0; padding: 0; box-sizing: border-box; }
  html, body {
    width: 1200px;
    height: 447px;
    overflow: hidden;
    background: var(--page);
  }
  .feed {
    position: relative;
    width: 1200px;
    height: 447px;
  }
  .post {
    position: absolute;
    top: 45px;
    width: 357px;
    height: 356px;
    overflow: hidden;
    color: var(--ink);
  }
  .post--one { left: 46px; }
  .post--two { left: 422px; }
  .post--three { left: 798px; }

  .post__photo {
    position: absolute;
    inset: 0;
  }
  .post--one .post__photo {
    background:
      linear-gradient(180deg, var(--paper-blush) 0%, var(--paper-light) 22%, var(--paper-light) 75%, var(--paper-mid) 100%);
  }
  .post--two .post__photo {
    background:
      radial-gradient(ellipse 60% 55% at 45% 30%, #8a8a8a 0%, transparent 70%),
      linear-gradient(160deg, #9b9b9b 0%, #8f8f8f 40%, #b9b9b9 70%, #dcdcdc 100%);
  }
  .post--three .post__photo {
    background:
      radial-gradient(ellipse 60% 50% at 50% 25%, #909090 0%, transparent 70%),
      linear-gradient(170deg, #a3a3a3 0%, #999999 45%, #c6c6c6 75%, #dedede 100%);
  }

  .post__quote {
    position: absolute;
    left: 16px;
    right: 8px;
    font-family: "Questrial", sans-serif;
    font-size: 20px;
    line-height: 27.5px;
    letter-spacing: 0.6px;
    text-transform: uppercase;
  }
  .post--one .post__quote { top: 70px; }
  .post--two .post__quote,
  .post--three .post__quote { top: 98px; }

  .accent {
    font-family: "Amatic SC", sans-serif;
    font-weight: 700;
    font-size: 27px;
    letter-spacing: 0;
  }

  .post__author {
    position: absolute;
    left: 16px;
    top: 226px;
    font-family: "Amatic SC", sans-serif;
    font-size: 36px;
    font-weight: 400;
    letter-spacing: 1px;
  }

  .post__brand {
    position: absolute;
    left: 0;
    right: 0;
    top: 278px;
    text-align: center;
    font-family: "Questrial", sans-serif;
    font-size: 11px;
    letter-spacing: 1px;
    text-transform: uppercase;
  }

  .post__band {
    position: absolute;
    left: 0;
    right: 0;
    bottom: 0;
    height: 54px;
    display: flex;
    align-items: center;
    justify-content: center;
    font-family: "Shadows Into Light", cursive;
    font-size: 30px;
  }
  .post--one .post__band { background: var(--band-light); }
  .post--two .post__band,
  .post--three .post__band { background: var(--band); }
</style>
</head>
<body>
<main class="feed">

  <article class="post post--one">
    <div class="post__photo" role="img" aria-label="Soft-focus photograph of an open book with pages curling at the edges"></div>
    <p class="post__quote">
      When you are<br>
      <span class="accent">Purpose</span>-driven<br>
      you live a fulfilling life<br>
      and you are true to<br>
      yourself.
    </p>
    <p class="post__author">– Mara Velleno</p>
    <p class="post__brand">The Lumen Compass</p>
    <p class="post__band">@thelumencompass</p>
  </article>

  <article class="post post--two">
    <div class="post__photo" role="img" aria-label="Close-up photograph of book pages folded into a heart shape"></div>
    <p class="post__quote">
      <span class="accent">Purpose</span>-driven means doing<br>
      whatever you are doing,<br>
      consciously thinking on<br>
      why it is important.
    </p>
    <p class="post__author">– Mara Velleno</p>
    <p class="post__brand">The Lumen Compass</p>
    <p class="post__band">@thelumencompass</p>
  </article>

  <article class="post post--three">
    <div class="post__photo" role="img" aria-label="Close-up photograph of curved book pages forming the right half of a heart"></div>
    <p class="post__quote">
      Companies and people who<br>
      are <span class="accent">Purpose</span>-driven maximize<br>
      their potential and impact<br>
      in the world.
    </p>
    <p class="post__author">– Mara Velleno</p>
    <p class="post__brand">The Lumen Compass</p>
    <p class="post__band">@thelumencompass</p>
  </article>

</main>
</body>
</html>
```